Verdant Loop Advisors, LLC

I am looking for a simple, clear layout with my logo prominent and embossed, on the best quality card stock available. I would like the business name and phone number included on the card as well......I dont want my name anywhere on the card and I would like my logo embossed on the card......something simple with a white back......open to designs as long as they go along with recycling symbols and green type stuff.....The address, website, cell number, fax number, and email are listed below

5374 Tillbury Fenwood Road
Hyattsville, MD 20785

c. 240.555.0143 f. 240.555.0187
e. sales@verdantloopadvisors.example
w. www.verdantloopadvisors.example

Industry/Entity Type

Recycling

```html
<!DOCTYPE html>
<html lang="en">
<head>
<meta charset="utf-8">
<title>Verdant Loop Advisors – Business Card</title>
<link rel="stylesheet" href="https://fonts.googleapis.com/css2?family=Open+Sans:wght@400;600;800&display=swap">
<style>
  :root {
    --backdrop: #d9d9d7;
    --card: #ffffff;
    --green: #1d5b33;
    --green-deep: #174a29;
    --ink: #2a2a2a;
    --panel-top: #f4f4f4;
    --panel-bottom: #dcdcdc;
    --rule: #c4c4c4;
    --cyan: #1fb3e6;
    --magenta: #e0267f;
    --yellow: #f3e61c;
  }
  * { box-sizing: border-box; margin: 0; padding: 0; }
  html, body { width: 1200px; height: 1131px; overflow: hidden; }
  body {
    background: var(--backdrop);
    font-family: "Open Sans", Arial, sans-serif;
    color: var(--ink);
    position: relative;
  }
  .card {
    position: absolute;
    top: 216px;
    width: 400px;
    height: 700px;
    background: var(--card);
    box-shadow: 0 6px 18px rgba(0,0,0,0.18);
    overflow: hidden;
  }
  .card--front { left: 150px; }
  .card--back { left: 650px; display: flex; flex-direction: column; }

  /* Front */
  .front-brand {
    position: absolute;
    top: 170px; left: 0; right: 0;
    display: flex; flex-direction: column; align-items: center;
  }
  .brand-square {
    width: 120px; height: 120px;
    background: var(--green);
    margin-bottom: 34px;
  }
  .brand-name {
    font-weight: 800;
    color: var(--ink);
    text-align: center;
    text-transform: uppercase;
    line-height: 1.1;
  }
  .brand-name__main { display: block; font-size: 38px; letter-spacing: 1px; }
  .brand-name__sub { display: block; font-size: 15px; letter-spacing: 7px; margin-top: 4px; }

  /* Back */
  .back-header {
    height: 96px;
    display: flex; align-items: center; justify-content: center; gap: 14px;
  }
  .back-header .brand-square { width: 40px; height: 40px; margin: 0; }
  .back-header .brand-name__main { font-size: 23px; }
  .back-header .brand-name__sub { font-size: 9px; letter-spacing: 4px; margin-top: 2px; }
  .print-stripe { display: flex; height: 6px; }
  .print-stripe span { flex: 1; }
  .print-stripe .cyan { background: var(--cyan); }
  .print-stripe .magenta { background: var(--magenta); }
  .print-stripe .yellow { background: var(--yellow); }

  .contact-panel {
    flex: 1;
    background: linear-gradient(180deg, var(--panel-top), var(--panel-bottom));
    padding: 10px 0 0;
  }
  .contact-row {
    display: flex; align-items: center; gap: 18px;
    height: 88px;
    padding: 0 24px;
    border-bottom: 1px solid var(--rule);
  }
  .contact-row:last-child { border-bottom: none; }
  .contact-icon {
    flex: 0 0 44px; width: 44px; height: 44px;
    border-radius: 50%;
    background: var(--green);
    display: flex; align-items: center; justify-content: center;
  }
  .contact-text { font-size: 16px; line-height: 1.25; }

  .pattern-band {
    height: 150px;
    background: linear-gradient(135deg, var(--green), var(--green-deep));
  }
</style>
</head>
<body>
  <section class="card card--front">
    <div class="front-brand">
      <div class="brand-square"></div>
      <p class="brand-name">
        <span class="brand-name__main">Verdant Loop</span>
        <span class="brand-name__sub">Advisors, LLC</span>
      </p>
    </div>
  </section>

  <section class="card card--back">
    <header class="back-header">
      <div class="brand-square"></div>
      <p class="brand-name">
        <span class="brand-name__main">Verdant Loop</span>
        <span class="brand-name__sub">Advisors, LLC</span>
      </p>
    </header>
    <div class="print-stripe"><span class="cyan"></span><span class="magenta"></span><span class="yellow"></span></div>

    <div class="contact-panel">
      <div class="contact-row">
        <div class="contact-icon">
          <svg width="22" height="22" viewBox="0 0 22 22" fill="none" stroke="#fff" stroke-width="2"><rect x="6" y="2" width="10" height="18" rx="2"/><line x1="10" y1="17" x2="12" y2="17"/></svg>
        </div>
        <p class="contact-text">c. 240.555.0143<br>f. 240.555.0187</p>
      </div>
      <div class="contact-row">
        <div class="contact-icon">
          <svg width="22" height="22" viewBox="0 0 22 22" fill="none" stroke="#fff" stroke-width="2"><rect x="2" y="5" width="18" height="12"/><path d="M2 5l9 7 9-7"/></svg>
        </div>
        <p class="contact-text">sales@verdantloopadvisors.example</p>
      </div>
      <div class="contact-row">
        <div class="contact-icon">
          <svg width="22" height="22" viewBox="0 0 22 22" fill="none" stroke="#fff" stroke-width="1.8"><circle cx="11" cy="11" r="9"/><ellipse cx="11" cy="11" rx="4" ry="9"/><line x1="2" y1="11" x2="20" y2="11"/></svg>
        </div>
        <p class="contact-text">www.verdantloopadvisors.example</p>
      </div>
      <div class="contact-row">
        <div class="contact-icon">
          <svg width="22" height="22" viewBox="0 0 22 22" fill="#fff"><path d="M11 1a7 7 0 0 0-7 7c0 5 7 13 7 13s7-8 7-13a7 7 0 0 0-7-7zm0 10a3 3 0 1 1 0-6 3 3 0 0 1 0 6z"/></svg>
        </div>
        <p class="contact-text">5374 Tillbury Fenwood Road<br>Hyattsville, MD 20785</p>
      </div>
    </div>

    <div class="pattern-band" role="img" aria-label="Band of repeated recycling arrow marks in white on green"></div>
  </section>
</body>
</html>
```